Website for Kitchen Showroom

We need a website for our Kitchen Showroom. Will be 10 pages in total. Example of a website we like can be found at http://www.velmarabo.co.uk/ with the image on the front page being a java script slideshow picking up images from a directory that I can update. Looking for simple SEO
I have the wording/ sitemap/ images all ready to go and I am looking for a quick turn around.
Thank you for your time. Rob

```html
<!DOCTYPE html>
<html lang="en">
<head>
<meta charset="utf-8">
<title>Hearthline Kitchens – Designer Kitchens</title>
<link href="https://fonts.googleapis.com/css2?family=Arimo:wght@400;700&display=swap" rel="stylesheet">
<style>
:root{
  --page:#ffffff;
  --header-top:#f7e9d0;
  --header-bottom:#efdcb9;
  --brand-grey:#8a8378;
  --green-light:#8fcb3f;
  --green:#6cb229;
  --green-dark:#4d8a16;
  --green-active:#3f7a0e;
  --text:#4a4a4a;
  --link:#3b6f10;
  --photo-light:#f6f1e6;
  --photo-mid:#e9e0cf;
  --photo-wood:#9a5a33;
}
*{box-sizing:border-box;margin:0;padding:0}
html,body{width:1149px;height:1200px;overflow:hidden;background:var(--page)}
body{position:relative;font-family:"Arimo",Arial,sans-serif;color:var(--text)}

.site-header{position:absolute;left:39px;top:13px;width:1075px;height:133px;border-radius:9px 9px 0 0;
  background:linear-gradient(var(--header-top),var(--header-bottom));border:1px solid #eadbbd}
.brand{position:absolute;left:18px;top:20px;display:flex;align-items:center;gap:14px}
.brand-mark{width:96px;height:96px;background:var(--green)}
.brand-name{font-size:48px;line-height:46px;font-weight:400;color:var(--brand-grey);letter-spacing:-1px}

.search{position:absolute;left:775px;top:48px;width:277px;height:42px;border-radius:21px;background:#fff;
  border:1px solid #c8bfae;box-shadow:inset 0 2px 4px rgba(0,0,0,.12);display:flex;align-items:center;padding:0 14px 0 18px}
.search span{flex:1;font-size:13px;color:#a8a8a8}

.main-nav{position:absolute;left:39px;top:146px;width:1075px;height:40px;border-radius:0 0 6px 6px;
  background:linear-gradient(var(--green-light),var(--green) 55%,var(--green-dark));
  box-shadow:0 3px 5px rgba(0,0,0,.25);display:flex}
.main-nav a{display:flex;align-items:center;justify-content:center;height:100%;color:#fff;text-decoration:none;
  font-size:13.5px;font-weight:700;border-right:1px solid rgba(255,255,255,.35)}
.main-nav a.active{background:linear-gradient(#5a9a1c,var(--green-active));border-radius:0 0 0 6px}
.social{position:absolute;top:5px;width:29px;height:29px;border-radius:3px}
.social.one{left:990px;background:#3b5998}
.social.two{left:1027px;background:#33b5e5}

.slideshow{position:absolute;left:39px;top:201px;width:1075px;height:667px;border-radius:9px;overflow:hidden;
  border:1px solid #cfcfcf;
  background:linear-gradient(to bottom,var(--photo-light) 0%,var(--photo-mid) 55%,#c08a5f 72%,var(--photo-wood) 100%)}
.slide-arrow{position:absolute;top:330px}
.slide-arrow.prev{left:22px}
.slide-arrow.next{right:22px}
.slide-pager{position:absolute;left:0;right:0;bottom:0;height:26px;background:rgba(120,100,90,.35);
  display:flex;justify-content:flex-end;align-items:center;gap:10px;padding-right:24px;font-size:12px;color:#111}

.intro{position:absolute;left:37px;top:886px;width:1080px}
.intro h1{font-size:25px;font-weight:400;color:var(--brand-grey);margin-bottom:14px}
.intro p{font-size:12.6px;line-height:20px;margin:0 0 20px 4px}
.intro a{color:var(--link)}

.site-footer{position:absolute;left:39px;top:1144px;width:1075px;height:37px;border-radius:4px;
  background:linear-gradient(var(--green-light),var(--green) 55%,var(--green-dark));
  box-shadow:0 3px 5px rgba(0,0,0,.25);color:#fff;font-size:12px;display:flex;align-items:center;justify-content:center}
</style>
</head>
<body>
<header class="site-header">
  <div class="brand">
    <div class="brand-mark"></div>
    <div class="brand-name">hearthline<br>kitchens</div>
  </div>
  <div class="search">
    <span>Search</span>
    <svg width="24" height="24" viewBox="0 0 24 24" fill="none" stroke="#9a9a9a" stroke-width="2">
      <circle cx="14" cy="10" r="7"/><line x1="9" y1="15" x2="3" y2="21"/>
    </svg>
  </div>
</header>

<nav class="main-nav">
  <a class="active" href="#" style="width:85px">HOME</a>
  <a href="#" style="width:108px">DESIGN</a>
  <a href="#" style="width:112px">GALLERY</a>
  <a href="#" style="width:114px">QUALITY</a>
  <a href="#" style="width:136px">CONTACT US</a>
  <a href="#" style="width:101px">LINKS</a>
  <span class="social one"></span>
  <span class="social two"></span>
</nav>

<section class="slideshow" role="img" aria-label="Bright white kitchen with island bench, stainless ovens and herringbone timber floor">
  <svg class="slide-arrow prev" width="38" height="40" viewBox="0 0 38 40"><polyline points="30,3 8,20 30,37" fill="none" stroke="#fff" stroke-width="8"/><polyline points="30,3 8,20 30,37" fill="none" stroke="#222" stroke-width="3"/></svg>
  <svg class="slide-arrow next" width="38" height="40" viewBox="0 0 38 40"><polyline points="8,3 30,20 8,37" fill="none" stroke="#fff" stroke-width="8"/><polyline points="8,3 30,20 8,37" fill="none" stroke="#222" stroke-width="3"/></svg>
  <div class="slide-pager"><span>01</span><span>02</span><span>03</span><span>04</span><span>05</span><span>06</span><span>07</span><span>08</span><span>09</span><span>10</span></div>
</section>

<main class="intro">
  <h1>Designer Kitchens by Hearthline Kitchens</h1>
  <p>Welcome to Hearthline Kitchens. WA's exclusive kitchen manufacturer based in Wanbrook Perth. If you are seeking the highest quality kitchen, yet at a price that is a little more affordable, Hearthline Kitchens is the company you've been searching for.</p>
  <p>Hearthline Kitchens showroom is located less than 25 kilometers from Perth CBD, so easy to get to with easy access from the Coastal Freeway.</p>
  <p>On this site, you can view some of our designer kitchens, read testimonials from our clients or just browse through our site to find out more. We hope you will find our site inspiring and put Hearthline Kitchens at the top of your list of kitchen showrooms you simply must visit.</p>
  <p>Pop into our showroom. We can chat about your plans and ideas for your new kitchen and maybe we can give you a few ideas of our own. Or <a href="#">contact us</a> to arrange a no obligation consultation with one of our kitchen designers and if required we will bring the showroom to you.</p>
</main>

<footer class="site-footer">© 2010 hearthlinekitchens. All Rights Reserved</footer>
</body>
</html>
```